Sudden Tides "Lantern Road" New Single Cover

Create cover artwork for the band Sudden Tides' new single "Lantern Road" being released early 2020. Style, font and graphics to be consistent with band's previous releases and overall brand identity. Visit www.suddentidesband.example and our Spotify page https://music.example.net/artist/7QzWpLx3RtVnKd8e2YbHcJ?si=MUrTgKa4PLe7skvWq2AmZd to view our previous releases and overall brand identity. Some examples attached as well. We are looking for someone to work with on future projects as well.

Lyrics are here: https://docs.example.org/document/d/3KTp9wrn_2ZQa8eXb4Lo_fimH7C5m83Jz4Pd70hrtVcA/edit

Music is here: https://audiostream.example.com/suddentides/lantern-road/s-pzkwa

Font styles to use
Sans Serif

Colors

Designer to choose colors to be used in the design.

Requirements
Must have
• Must be consistent with current brand identity and with prior album / single art.

```html
<!DOCTYPE html>
<html lang="en">
<head>
<meta charset="utf-8">
<title>Sudden Tides – Lantern Road</title>
<link rel="stylesheet" href="https://fonts.googleapis.com/css2?family=Josefin+Sans:wght@300;600&display=swap">
<style>
  :root {
    --bg-purple: #5c2d7f;
    --disc-glow: #7b2d7f;
    --disc-mid: #6c3088;
    --disc-edge: #623393;
    --accent-pink: #d5709d;
  }
  html, body {
    margin: 0;
    padding: 0;
    width: 1200px;
    height: 1200px;
    overflow: hidden;
    background: var(--bg-purple);
  }
  .cover {
    position: relative;
    width: 1200px;
    height: 1200px;
    background: var(--bg-purple);
  }
  .wall-disc {
    position: absolute;
    left: 207px;
    top: 207px;
    width: 786px;
    height: 786px;
  }
  .single-title {
    position: absolute;
    left: 0;
    right: 0;
    top: 556px;
    margin: 0;
    text-align: center;
    font-family: "Josefin Sans", sans-serif;
    font-weight: 600;
    font-size: 68px;
    line-height: 1;
    letter-spacing: 0.2em;
    padding-left: 0.2em;
    color: var(--accent-pink);
    text-transform: uppercase;
  }
  .band-name {
    position: absolute;
    left: 0;
    right: 0;
    top: 1072px;
    margin: 0;
    text-align: center;
    font-family: "Josefin Sans", sans-serif;
    font-weight: 300;
    font-size: 52px;
    line-height: 1;
    letter-spacing: 0.08em;
    padding-left: 0.08em;
    color: var(--accent-pink);
    text-transform: uppercase;
  }
</style>
</head>
<body>
  <main class="cover">
    <svg class="wall-disc" viewBox="0 0 786 786" role="img" aria-label="Round window onto a purple brick wall, softly lit from the upper left">
      <defs>
        <radialGradient id="disc-light" cx="0.32" cy="0.32" r="0.8">
          <stop offset="0" stop-color="var(--disc-glow)"/>
          <stop offset="0.55" stop-color="var(--disc-mid)"/>
          <stop offset="1" stop-color="var(--disc-edge)"/>
        </radialGradient>
      </defs>
      <circle cx="393" cy="393" r="393" fill="url(#disc-light)"/>
    </svg>
    <h1 class="single-title">Lantern Road</h1>
    <p class="band-name">Sudden Tides</p>
  </main>
</body>
</html>
```